Design my dad a new business card because his current one sucks!

I need a business card designed for my fathers home maintenance business. His customers are individuals (single moms, old people etc.) as well as the occasional business. As such it needs to be accessible to both target audiences.

The front of the card should be dark grey on yellow with the logo and contain the following information:
- Darren Whitlock
- 0488 372 915
- info@bluegumhomecare.example.au
- 0488 372 915

- ABN: 71 284 630 912
- 'Fully Insured'

The reverse should be yellow on dark grey and will have the web address:
- bluegumhomecare.example.au

And a few key services he offers:
GENERAL REPAIRS
PAINTING/TILING/
PAVING &CONCRETING
PRESSURE WASHING
ON-SITE WELDING
DECKING ADDITIONS & REPAIRS
FENCING
FULL BOND CLEANING

This will be first time the logo has been printed so you will need to come up with the best CMYK approximation of the RGB colours to make sure it is a close as possible.

```html
<!DOCTYPE html>
<html lang="en">
<head>
<meta charset="utf-8">
<title>Bluegum Home Care – Business Card</title>
<link href="https://fonts.googleapis.com/css2?family=Open+Sans:wght@400;600;700&display=swap" rel="stylesheet">
<style>
  :root {
    --yellow: #f7dc1e;
    --yellow-deep: #f0cc14;
    --charcoal: #2b2b2b;
    --stripe: #e6e6e6;
    --white: #ffffff;
    --backdrop: #d9d9d9;
  }
  * { box-sizing: border-box; margin: 0; padding: 0; }
  html, body { width: 1200px; height: 1096px; overflow: hidden; }
  body {
    background: var(--backdrop);
    font-family: "Open Sans", Arial, sans-serif;
    position: relative;
  }
  .card {
    position: absolute;
    left: 180px;
    width: 840px;
    height: 490px;
    overflow: hidden;
    box-shadow: 0 6px 18px rgba(0,0,0,.18);
  }

  /* ---------- Reverse ---------- */
  .card--reverse { top: 40px; background: linear-gradient(160deg, var(--yellow) 0%, var(--yellow-deep) 100%); }
  .card--reverse .brand { position: absolute; left: 330px; top: 70px; color: var(--charcoal); }
  .card--reverse .services-left { position: absolute; left: 40px; top: 196px; color: var(--charcoal); }
  .card--reverse .stripe { position: absolute; left: 0; top: 300px; width: 100%; height: 12px; background: var(--stripe); }
  .card--reverse .dark-panel { position: absolute; left: 0; top: 312px; width: 500px; height: 178px; background: var(--charcoal); }
  .card--reverse .dark-foot { position: absolute; left: 0; top: 440px; width: 100%; height: 50px; background: var(--charcoal); }
  .card--reverse .foot-stripe { position: absolute; left: 500px; top: 430px; width: 340px; height: 10px; background: var(--stripe); }
  .card--reverse .web { position: absolute; left: 40px; top: 340px; color: var(--white); font-size: 17px; letter-spacing: .3px; }
  .card--reverse .services-right { position: absolute; right: 40px; top: 328px; color: var(--charcoal); text-align: right; }

  .services { font-size: 15px; line-height: 1.3; font-weight: 400; letter-spacing: .8px; text-transform: uppercase; }

  .brand { display: flex; align-items: center; gap: 16px; font-weight: 700; }
  .brand__dot { width: 54px; height: 54px; border-radius: 50%; background: currentColor; flex: none; }
  .brand__name { font-size: 62px; line-height: 1.2; letter-spacing: -1px; }
  .brand__sub { font-size: 22px; line-height: 1.1; letter-spacing: 3px; text-transform: uppercase; margin-top: 4px; }

  /* ---------- Front ---------- */
  .card--front { top: 566px; background: var(--charcoal); }
  .card--front .brand { position: absolute; left: 40px; top: 60px; color: var(--yellow); }
  .card--front .name { position: absolute; right: 50px; top: 70px; color: var(--white); font-size: 24px; letter-spacing: .5px; text-transform: uppercase; }
  .card--front .yellow-field { position: absolute; left: 0; top: 250px; width: 100%; height: 240px; background: var(--yellow); }
  .card--front .stripe-a { position: absolute; left: 0; top: 362px; width: 100%; height: 12px; background: var(--stripe); }
  .card--front .dark-band { position: absolute; left: 0; top: 374px; width: 100%; height: 12px; background: var(--charcoal); }
  .card--front .stripe-b { position: absolute; left: 0; top: 440px; width: 100%; height: 8px; background: var(--stripe); }
  .card--front .credentials { position: absolute; left: 40px; top: 272px; color: var(--charcoal); font-size: 16px; line-height: 1.6; }
  .contact { position: absolute; color: var(--charcoal); font-size: 16px; list-style: none; }
  .contact li { display: flex; align-items: center; gap: 12px; height: 28px; }
  .contact svg { width: 16px; height: 16px; fill: var(--charcoal); flex: none; }
  .contact--phone { left: 250px; top: 280px; }
  .contact--online { left: 470px; top: 280px; }
</style>
</head>
<body>

<section class="card card--reverse" aria-label="Card reverse">
  <div class="brand">
    <span class="brand__dot"></span>
    <div>
      <div class="brand__name">Bluegum</div>
      <div class="brand__sub">Home Care</div>
    </div>
  </div>
  <p class="services services-left">General Repairs<br>Painting/Tiling/<br>Paving &amp;Concreting<br>Pressure Washing</p>
  <div class="stripe"></div>
  <div class="dark-panel"></div>
  <div class="foot-stripe"></div>
  <div class="dark-foot"></div>
  <p class="web">www.bluegumhomecare.example.au</p>
  <p class="services services-right">On-Site Welding<br>Decking Additions &amp; Repairs<br>Fencing<br>Full Bond Cleaning</p>
</section>

<section class="card card--front" aria-label="Card front">
  <div class="brand">
    <span class="brand__dot"></span>
    <div>
      <div class="brand__name">Bluegum</div>
      <div class="brand__sub">Home Care</div>
    </div>
  </div>
  <p class="name">Darren Whitlock</p>
  <div class="yellow-field"></div>
  <div class="stripe-a"></div>
  <div class="dark-band"></div>
  <div class="stripe-b"></div>
  <p class="credentials">ABN: 71 284 630 912<br>'Fully Insured'</p>
  <ul class="contact contact--phone">
    <li><svg viewBox="0 0 16 16" aria-hidden="true"><path d="M4 1l2 3-1.5 1.5c.8 2 2.6 3.8 4.5 4.5L10.5 8.5l3 2-1 3c-5 0-10-5-10-10z"/></svg>0488 372 915</li>
    <li><svg viewBox="0 0 16 16" aria-hidden="true"><rect x="4" y="1" width="8" height="5"/><rect x="1" y="6" width="14" height="6" rx="1"/><rect x="4" y="11" width="8" height="4"/></svg>0488 372 915</li>
  </ul>
  <ul class="contact contact--online">
    <li><svg viewBox="0 0 16 16" aria-hidden="true"><circle cx="8" cy="8" r="7" fill="none" stroke="#2b2b2b" stroke-width="1.5"/><ellipse cx="8" cy="8" rx="3" ry="7" fill="none" stroke="#2b2b2b" stroke-width="1.2"/><path d="M1 8h14" stroke="#2b2b2b" stroke-width="1.2"/></svg>bluegumhomecare.example.au</li>
    <li><svg viewBox="0 0 16 16" aria-hidden="true"><rect x="1" y="3" width="14" height="10" fill="none" stroke="#2b2b2b" stroke-width="1.5"/><path d="M1 3l7 6 7-6" fill="none" stroke="#2b2b2b" stroke-width="1.5"/></svg>info@bluegumhomecare.example.au</li>
  </ul>
</section>

</body>
</html>
```